Webbanner-Design holvira.at Webshop
Zielgruppe
Onlineshop für Haus + Garten
holvira.at
Aufgabenstellung
Benötigt wird ein neues Banner-Set
ein Allgemeines - warum bei holvira.at einkaufen
- günstige Preise durch Direktbezug ohne Zwischenhandel
- alle Artikel vorrätig - schnelle Lieferung
- Sichere Kaufabwicklung - Lumena Kauf
- Fachberatung und Service durch geschultes Peronal
sowie Banner für jede Hauptkategorie

```html
<!DOCTYPE html>
<html lang="de">
<head>
<meta charset="utf-8">
<title>holvira.at – Webshop</title>
<link href="https://fonts.googleapis.com/css2?family=Open+Sans:wght@400;600;700;800&display=swap" rel="stylesheet">
<style>
  :root{
    --link:#3a8fd4;
    --gold:#c9a95c;
    --blue-dark:#1e3f86;
    --blue:#2660a8;
    --text:#555;
    --nav-bg-top:#ffffff;
    --nav-bg-bottom:#ececec;
    --white:#ffffff;
  }
  *{box-sizing:border-box;margin:0;padding:0}
  html,body{width:1200px;height:745px;overflow:hidden}
  body{font-family:"Open Sans",sans-serif;background:var(--white);position:relative}
  .header{position:absolute;left:0;top:0;width:1200px;height:110px;background:var(--white)}
  .brand{position:absolute;left:58px;top:38px;display:flex;align-items:center;gap:8px;
    font-family:"Open Sans",sans-serif;font-weight:700;font-size:26px;color:var(--gold)}
  .brand-mark{width:20px;height:20px;background:var(--blue-dark)}
  .seal{position:absolute;left:342px;top:36px;width:52px;height:52px;border-radius:50%;
    background:var(--blue-dark);border:4px solid var(--white);box-shadow:0 0 0 2px var(--blue-dark)}
  .meta-links{position:absolute;left:892px;top:14px;display:flex;font-size:12px;color:var(--link)}
  .meta-links span{padding:0 7px;border-left:1px solid #ccc}
  .meta-links span:first-child{padding-left:0;border-left:none}
  .lang{position:absolute;left:1069px;top:13px;width:77px;height:21px;background:#444;border:1px solid #222;
    border-radius:3px;color:#fff;font-size:11.5px;line-height:19px;padding-left:18px}
  .search{position:absolute;left:676px;top:49px;width:242px;height:36px;border:1px solid #ccc;border-radius:3px;
    font-size:13px;color:#999;line-height:34px;padding-left:12px}
  .search-btn{position:absolute;right:-1px;top:-1px;width:41px;height:36px;background:#eee;border:1px solid #ccc;
    border-radius:0 3px 3px 0}
  .account,.cart{position:absolute;top:64px;font-size:14px;color:var(--link)}
  .account{left:947px}
  .cart{left:1069px}
  .nav{position:absolute;left:0;top:110px;width:1200px;height:61px;
    background:linear-gradient(var(--nav-bg-top),var(--nav-bg-bottom))}
  .nav span{position:absolute;top:20px;font-size:13.5px;color:var(--text)}
  .stage{position:absolute;left:0;top:171px;width:1200px;height:574px;
    background:linear-gradient(90deg,#6d9aa8 0%,#a7c8d3 8%,#cfe2e8 50%,#a9c7d0 92%,#3f7e90 100%)}
  .panel{position:absolute;left:50px;top:185px;width:1100px;height:549px;background:var(--white)}
  .banner{position:absolute;left:73px;top:207px;width:1055px;height:439px}
  .banner-text{position:absolute;left:38px;color:var(--white);font-weight:700}
  .kicker{top:35px;font-size:16px;font-weight:400}
  .kicker b{font-weight:700}
  .headline{top:84px;font-size:35px;line-height:41px;font-weight:800}
  .features{top:185px;font-size:22px;line-height:28.5px;font-weight:700;list-style:none}
  .features li::before{content:"";display:inline-block;width:9px;height:9px;border-top:4px solid var(--gold);
    border-right:4px solid var(--gold);transform:rotate(45deg);margin-right:10px;margin-bottom:3px}
  .cta{position:absolute;left:38px;top:358px;width:155px;height:44px;background:var(--gold);color:var(--white);
    font-size:12px;font-weight:700;text-align:center;line-height:44px}
  .offer{position:absolute;left:890px;top:274px;width:128px;height:128px;border-radius:50%;background:var(--gold);
    color:var(--white);text-align:center;font-weight:700}
  .offer small{display:block;margin-top:37px;font-size:11px;line-height:17px}
  .offer strong{display:block;font-size:24px;line-height:30px}
  .dots{position:absolute;left:520px;top:686px;display:flex;gap:18px}
  .dots i{width:7px;height:7px;border-radius:50%;background:#333}
  .dots i.active{width:10px;height:10px;margin-top:-1.5px;background:none;border:2px solid #333}
</style>
</head>
<body>
  <header class="header">
    <div class="brand"><span class="brand-mark"></span>holvira.at</div>
    <div class="seal" role="img" aria-label="Gütesiegel"></div>
    <nav class="meta-links"><span>News</span><span>Kontakt</span><span>Links</span></nav>
    <div class="lang">Deutsch ▾</div>
    <div class="search">Suchen
      <div class="search-btn">
        <svg width="41" height="36" viewBox="0 0 41 36"><circle cx="19" cy="16" r="6" fill="none" stroke="#3a8fd4" stroke-width="2.5"/><line x1="23.5" y1="20.5" x2="28" y2="25" stroke="#3a8fd4" stroke-width="2.5"/></svg>
      </div>
    </div>
    <div class="account">● Anmelden ▾</div>
    <div class="cart">🛒︎ 0,00 € ▾</div>
  </header>
  <nav class="nav">
    <span style="left:64px">Badezimmer ▾</span>
    <span style="left:183px">Schwimmbecken ▾</span>
    <span style="left:328px">Schwimmbadzubehör ▾</span>
    <span style="left:505px">Sauna</span>
    <span style="left:572px">Heizung, Solar, Klima ▾</span>
    <span style="left:743px">Garten ▾</span>
    <span style="left:826px">Kabelkanal</span>
    <span style="left:923px">Whirlpoolzubehör ▾</span>
  </nav>
  <div class="stage"></div>
  <div class="panel"></div>
  <section class="banner">
    <svg width="1055" height="439" viewBox="0 0 1055 439">
      <defs>
        <linearGradient id="photoTone" x1="0" y1="0" x2="0" y2="1">
          <stop offset="0" stop-color="#5f7a3a"/>
          <stop offset="0.4" stop-color="#8a8a6a"/>
          <stop offset="0.7" stop-color="#8c6a55"/>
          <stop offset="1" stop-color="#c8bfae"/>
        </linearGradient>
        <linearGradient id="blueTone" x1="0" y1="0" x2="1" y2="1">
          <stop offset="0" stop-color="#1e3f86"/>
          <stop offset="1" stop-color="#2766ad"/>
        </linearGradient>
      </defs>
      <rect width="1055" height="439" fill="url(#photoTone)" role="img" aria-label="Foto: Gartenlounge mit Kissen, Kerzen und Blumen"/>
      <path d="M0 0 H510 Q358 219 500 439 H0 Z" fill="#c9a95c"/>
      <path d="M0 0 H493 Q310 220 479 439 H0 Z" fill="url(#blueTone)"/>
    </svg>
    <p class="banner-text kicker"><b>IHR FACHMANN</b> FÜR BAD, POOL UND MEHR</p>
    <h1 class="banner-text headline">IHR PERSÖNLICHES<br>GARTENPARADIES</h1>
    <ul class="banner-text features">
      <li>GARTENMÖBEL</li>
      <li>TERRASSENDIELEN</li>
      <li>SOLARDUSCHEN UVM.</li>
    </ul>
    <div class="cta">ENTDECKEN</div>
    <div class="offer"><small>HOCHWERTIGES<br>ZUBEHÖR AB NUR</small><strong>59,99€</strong></div>
  </section>
  <div class="dots"><i></i><i></i><i></i><i></i><i class="active"></i><i></i><i></i></div>
</body>
</html>
```